Trade Show booth design

I need the following designs for my trade booth:
1. backboard design 3m Wx2mH
2. Tressle table, tablecloth front panel design 1800W x 740mmH
3. Pop-up banner. I have included our logos and some design content ideas:
Headline:
"Cleaner Classrooms. Safer Schools."
Subheadline:
"Specialist Cleaning Solutions for Education Facilities"
Key Points to Grab Attention:
Healthy Environments: Create hygienic, safe learning spaces for students and staff with our expert cleaning services.
Tailored to Your Needs: Custom cleaning plans for classrooms, labs, libraries, and sports facilities.
Affordable Excellence: Premium results without premium costs – tailored plans mean you only pay for what you need.
Safety First: All staff are trained, highly vetted, and hold current Working with Children Checks (WWCC).
Eco-Conscious Cleaning: Using non-toxic, eco-friendly products certified for health and safety.
What Schools Really Need:
Reliability: Consistent, high-quality cleaning from a trusted provider.
Cost-Effectiveness: Solutions that fit tight budgets while maintaining high standards.
Expertise: Over 30 years of experience in education facility cleaning.
Disinfection Services: Focus on high-touch areas to reduce the spread of germs and ensure peace of mind.
Visual Elements:
Images of bright, clean classrooms, a happy teacher welcoming students, or students collaborating in a spotless library.
Icons representing safety (shield), hygiene (sparkling star), and eco-friendliness (leaf).
Your logo with the tagline: "Trusted by Queensland Schools Since 1995."
Call-to-Action:
"Visit us to discuss your school’s cleaning needs and book a FREE consultation."
Include contact details: Phone: 1300 649 315 | Website: www.duravoss.com.au
Target Market(s)
Education sector
Industry/Entity Type
Commercial Cleaning
Font styles to use
Other font styles liked:
- Montserrat
Look and feel

```html
<!DOCTYPE html>
<html lang="en">
<head>
<meta charset="utf-8">
<title>Duravoss – Education Cleaning Backdrop</title>
<link href="https://fonts.googleapis.com/css2?family=Montserrat:wght@400;500;600;700;800&display=swap" rel="stylesheet">
<style>
  :root{
    --navy:#1f3b5c;
    --navy-deep:#15304f;
    --ink:#1b1f24;
    --silver:#c4c7ca;
    --lime:#b8dc6a;
    --paper:#f3f4f5;
    --white:#ffffff;
  }
  *{margin:0;padding:0;box-sizing:border-box}
  html,body{width:1200px;height:960px;overflow:hidden;background:var(--paper)}
  body{font-family:'Montserrat',sans-serif;color:var(--ink)}
  .backdrop{position:relative;width:1200px;height:960px;overflow:hidden;
    background:linear-gradient(180deg,#ffffff 0%,#eef0f1 40%,#e6e8ea 100%)}
  .classroom-photo{position:absolute;left:0;top:395px;width:1200px;height:565px;
    background:linear-gradient(180deg,rgba(243,245,246,0) 0%,#e9eced 30%,#dfe4e2 48%,#cfe49c 62%,#c7df8a 72%,#e3eadb 86%,#d8dcdc 100%)}
  .brand{position:absolute;top:88px;left:0;width:1200px;display:flex;justify-content:center;align-items:center;gap:18px}
  .brand-dot{width:54px;height:54px;border-radius:50%;background:var(--navy)}
  .brand-name{font-weight:700;font-size:52px;letter-spacing:4px;color:var(--navy)}
  .headline{position:absolute;top:212px;left:0;width:1200px;text-align:center;
    font-weight:800;font-size:57px;line-height:56px;color:var(--navy);text-transform:uppercase;letter-spacing:.5px}
  .subhead{position:absolute;top:348px;left:95px;width:1020px;height:40px}
  .subhead-bar{position:absolute;inset:4px 0 0 0;background:linear-gradient(90deg,#a9adb1,#cfd2d4 60%,#b9bcbf);
    border-radius:14px 6px 14px 6px;transform:skewX(-12deg)}
  .subhead-text{position:relative;text-align:center;font-weight:500;font-size:25px;line-height:36px;color:var(--navy)}
  .features{position:absolute;top:405px;left:0;width:1200px}
  .feature{position:absolute;width:230px;text-align:center;font-size:16.5px;line-height:21px;color:var(--ink)}
  .feature b{font-weight:700}
  .feature-icon{width:82px;height:82px;margin:0 auto 20px;border-radius:50%;background:var(--navy);
    box-shadow:0 0 0 5px rgba(200,204,208,.7);display:flex;align-items:center;justify-content:center}
  .feature--experience{left:248px}
  .feature--trust{left:491px}
  .feature--eco{left:727px}
  .footer-band{position:absolute;left:0;top:0}
  .cta{position:absolute;right:37px;top:760px;text-align:right;color:var(--white)}
  .cta-line{font-weight:500;font-size:22px;line-height:28px}
  .cta-url{margin-top:10px;font-weight:500;font-size:54px;line-height:60px;letter-spacing:.5px}
</style>
</head>
<body>
<main class="backdrop">
  <div class="classroom-photo" role="img" aria-label="Bright, clean classroom with rows of lime green desks and chairs and sunny windows"></div>

  <svg class="footer-band" width="1200" height="960" viewBox="0 0 1200 960" aria-hidden="true">
    <defs>
      <linearGradient id="navyFill" x1="0" y1="0" x2="1" y2="1">
        <stop offset="0" stop-color="#2a4869"/>
        <stop offset="1" stop-color="#15304f"/>
      </linearGradient>
    </defs>
    <path d="M0 820 C380 820 720 680 1200 660 L1200 960 L0 960Z" fill="url(#navyFill)"/>
  </svg>

  <header class="brand">
    <span class="brand-dot"></span>
    <span class="brand-name">DURAVOSS</span>
  </header>

  <h1 class="headline">Creating Cleaner,<br>Safer Learning Environments</h1>

  <div class="subhead">
    <div class="subhead-bar"></div>
    <p class="subhead-text">Specialists in Education Facility Cleaning &amp; Eco-Friendly Services</p>
  </div>

  <section class="features">
    <div class="feature feature--experience">
      <div class="feature-icon">
        <svg width="40" height="40" viewBox="0 0 40 40" fill="none" stroke="#fff" stroke-width="2.5" stroke-linecap="round" stroke-linejoin="round"><circle cx="20" cy="20" r="15"/><path d="M13 20.5l5 5 9-10"/></svg>
      </div>
      <p>Over <b>30 years</b><br>of expertise in<br>commercial cleaning.</p>
    </div>
    <div class="feature feature--trust">
      <div class="feature-icon">
        <svg width="40" height="40" viewBox="0 0 40 40" fill="none" stroke="#fff" stroke-width="2.2" stroke-linejoin="round"><path d="M20 5l4.4 9 9.8 1.4-7.1 6.9 1.7 9.8L20 27.5l-8.8 4.6 1.7-9.8-7.1-6.9 9.8-1.4z"/></svg>
      </div>
      <p>Trusted by <b>schools,<br>universities, and TAFEs</b><br>across Queensland.</p>
    </div>
    <div class="feature feature--eco">
      <div class="feature-icon">
        <svg width="40" height="40" viewBox="0 0 40 40" fill="none" stroke="#fff" stroke-width="2.4" stroke-linecap="round" stroke-linejoin="round"><path d="M8 30C8 15 18 8 33 8c0 15-8 24-22 22z"/><path d="M8 32L24 16"/></svg>
      </div>
      <p><b>100% Carbon Neutral<br>and Eco-Certified</b><br>Services.</p>
    </div>
  </section>

  <footer class="cta">
    <p class="cta-line">Visit us to discuss your school’s cleaning needs<br>and book a FREE consultation.</p>
    <p class="cta-url">www.duravoss.com.au</p>
  </footer>
</main>
</body>
</html>
```